Zenvok - Property Management Company Listings - PSD / uncoded only

Our site simply connects property owners with property managers. I’m asking you to create 2 pages, 1 homepage and 1 page that lists of property management companies. Build with Responsive Design in mind. PSD/uncoded files only. Help us create a great site!
Example competitor sites:
http://www.everyleaseguildhall.example/
http://www.tendourestates.example/
Inspired by these sites:
http://www.quorvix.example/
http://www.bespokuna.example/
http://www.fundlo.example/
https://www.tripnook.example/
I've attached the logo as well as 2 picture files that you can consider using.
• Zenvok Logo Colors: Yellow: HTML code: #FBC30A, RGB code: R: 251 G: 195 B: 10 Grey: HTML code: #4E4C4D, RGB code: R: 78 G: 76 B: 77
• The picture files are optional.
o One picture is of houses and neighborhood.
o The other is of a professional woman on the phone. Please do not use the professional woman as a large primary image. You can use the professional woman photo as a smaller photo and not the main photo.
• Please bring your own pictures and graphics too. Don't feel like you need to use mine.
Thank you!
Property Management

```html
<!DOCTYPE html>
<html lang="en">
<head>
<meta charset="utf-8">
<title>Zenvok – Property Management</title>
<link rel="stylesheet" href="https://fonts.googleapis.com/css2?family=Ubuntu:wght@400;500;700&family=Arimo:wght@400;700&display=swap">
<style>
:root{
  --yellow:#ffcc00;
  --brand-yellow:#fbc30a;
  --grey:#4e4c4d;
  --dark:#232323;
  --darker:#1a1a1a;
  --panel:rgba(28,28,28,.92);
  --text:#333;
  --white:#fff;
}
*{box-sizing:border-box;margin:0;padding:0}
html,body{width:835px;height:1200px;overflow:hidden;background:var(--white)}
body{position:relative;font-family:"Arimo",Arial,sans-serif;color:var(--text)}

/* header */
.site-header{position:absolute;left:0;top:0;width:835px;height:80px;background:var(--white)}
.brand{position:absolute;left:70px;top:14px;display:flex;align-items:center;gap:8px}
.brand-mark{width:16px;height:16px;background:var(--brand-yellow)}
.brand-name{font-family:"Ubuntu",sans-serif;font-weight:700;font-size:38px;color:var(--grey);letter-spacing:-1px;line-height:1}
.call{position:absolute;left:450px;top:33px;font-family:"Arimo",sans-serif;font-size:15px;display:flex;align-items:center;gap:6px}
.call .label{color:var(--brand-yellow)}
.call .num{color:#222;margin-left:4px}
.social{position:absolute;left:648px;top:29px;display:flex;gap:5px}
.social span{width:24px;height:24px;border-radius:50%}

/* nav */
.main-nav{position:absolute;left:0;top:80px;width:835px;height:36px;background:var(--yellow)}
.main-nav a{position:absolute;top:6px;height:24px;line-height:24px;font-family:"Ubuntu",sans-serif;font-weight:500;font-size:12px;color:#333;text-decoration:none;letter-spacing:.3px}
.main-nav .active{left:70px;width:56px;text-align:center;background:#3a3a3a;color:var(--white)}

/* hero */
.hero{position:absolute;left:0;top:116px;width:835px;height:330px;background:linear-gradient(160deg,#5b5750 0%,#3f3d3a 45%,#4f4a44 100%)}
.hero-photo{position:absolute;left:97px;top:56px;width:343px;height:229px;background:linear-gradient(90deg,#c9c4b8 0%,#e9e6df 55%,#a7a19a 100%)}
.search-panel{position:absolute;left:440px;top:56px;width:280px;height:229px;background:var(--panel);color:var(--white)}
.search-panel h1{position:absolute;left:22px;top:20px;font-family:"Ubuntu",sans-serif;font-weight:500;font-size:20px;color:var(--yellow)}
.field-label{position:absolute;left:25px;font-size:12px;line-height:14px;color:var(--white)}
.select{position:absolute;left:25px;top:82px;width:221px;height:24px;background:var(--white)}
.select::after{content:"▼";position:absolute;right:6px;top:5px;font-size:10px;color:#111}
.zip{position:absolute;left:25px;top:143px;width:144px;height:24px;background:var(--white)}
.btn-search{position:absolute;left:147px;top:185px;width:105px;height:28px;border-radius:3px;background:linear-gradient(#ffd83a,#e9b300);font-family:"Ubuntu",sans-serif;font-weight:700;font-size:15px;letter-spacing:1px;color:#222;text-align:center;line-height:28px}

/* steps */
.step{position:absolute;top:488px;width:200px;text-align:center}
.step-num{width:62px;height:62px;margin:0 auto;border-radius:50%;background:var(--yellow);border:2px solid #333;font-family:"Ubuntu",sans-serif;font-weight:500;font-size:23px;line-height:58px;color:#222}
.step p{margin-top:20px;font-size:10px;line-height:14px;color:#333}

/* agents & reviews */
.agents-band{position:absolute;left:0;top:691px;width:835px;height:269px;background:var(--yellow)}
.section-title{position:absolute;font-family:"Ubuntu",sans-serif;font-weight:500;font-size:22px;color:#111}
.title-rule{position:absolute;left:205px;top:32px;width:303px;height:1px;background:#333}
.agent{position:absolute;top:64px;width:134px;height:180px;background:var(--white);border:1px solid #f0e3a0;text-align:center}
.agent-photo{width:104px;height:104px;border-radius:50%;margin:11px auto 0}
.agent-name{margin-top:13px;font-family:"Ubuntu",sans-serif;font-size:10.5px;color:#222}
.agent-sub{margin-top:2px;font-size:6.5px;color:#aaa}
.stars{margin-top:8px;font-size:10px;color:var(--brand-yellow)}
.stars .off{color:#e7d690}
.review{position:absolute;left:546px;width:200px}
.review h3{font-size:9.5px;font-weight:700;color:#111}
.review p{margin-top:4px;font-size:9px;line-height:11.5px;color:#111}

/* footer */
.site-footer{position:absolute;left:0;top:960px;width:835px;height:213px;background:var(--dark);color:var(--white)}
.f-head{position:absolute;top:23px;font-family:"Arimo",sans-serif;font-weight:700;font-size:11.5px;color:var(--yellow);white-space:nowrap}
.f-links{position:absolute;top:48px;list-style:none;font-family:"Ubuntu",sans-serif;font-size:8px;line-height:16.6px}
.f-phone{position:absolute;left:263px;top:39px;font-family:"Ubuntu",sans-serif;font-weight:500;font-size:17px}
.f-mail{position:absolute;left:263px;top:65px;font-family:"Ubuntu",sans-serif;font-size:8px}
.f-place{position:absolute;left:263px;top:84px;display:flex;gap:5px;font-family:"Ubuntu",sans-serif}
.f-place strong{display:block;font-weight:500;font-size:11px}
.f-place small{display:block;font-size:7px;font-weight:500}
.f-social{position:absolute;left:263px;top:135px;display:flex;gap:8px}
.f-social span{width:16px;height:16px;border-radius:2px}
.f-note{position:absolute;left:81px;top:168px;width:372px;font-family:"Ubuntu",sans-serif;font-size:6.7px;line-height:13px;color:#6f6f6f}
.f-label{position:absolute;font-size:8.5px;font-weight:700}
.f-input{position:absolute;background:var(--white);border:1px solid #ccc}
.btn-send{position:absolute;left:464px;top:180px;width:100px;height:21px;background:var(--yellow);font-size:9.5px;color:#333;text-align:center;line-height:21px}
.copyright{position:absolute;left:0;top:1173px;width:835px;height:27px;background:var(--darker);color:#ddd;font-size:9.5px;text-align:center;line-height:27px}
</style>
</head>
<body>

<header class="site-header">
  <div class="brand"><span class="brand-mark"></span><span class="brand-name">zenvok</span></div>
  <div class="call">
    <svg width="18" height="18" viewBox="0 0 18 18" aria-hidden="true"><rect x="3" y="3" width="12" height="13" rx="1.5" fill="none" stroke="#333" stroke-width="1.6"/><rect x="6" y="5" width="6" height="3" fill="#333"/><circle cx="7" cy="11" r="1" fill="#333"/><circle cx="11" cy="11" r="1" fill="#333"/><circle cx="7" cy="14" r="1" fill="#333"/><circle cx="11" cy="14" r="1" fill="#333"/></svg>
    <span class="label">Call Us</span><span class="num">800 512 40 76</span>
  </div>
  <div class="social" aria-label="Social links">
    <span style="background:#1f5ea8"></span><span style="background:#2aa9e0"></span><span style="background:#f39a1f"></span><span style="background:#d6352b"></span>
  </div>
</header>

<nav class="main-nav">
  <a class="active" href="#">HOME</a>
  <a href="#" style="left:150px">ARE YOU A PROPERTY MANAGER?</a>
  <a href="#" style="left:370px">CONTACT US</a>
</nav>

<section class="hero" role="img" aria-label="Aerial view of suburban houses and neighborhood">
  <div class="hero-photo" role="img" aria-label="Professional woman in a business suit talking on the phone"></div>
  <div class="search-panel">
    <h1>Find your Local Property</h1>
    <span class="field-label" style="top:61px">Select Your Property Type</span>
    <div class="select"></div>
    <span class="field-label" style="top:122px">In Zipcode</span>
    <div class="zip"></div>
    <div class="btn-search">SEARCH</div>
  </div>
</section>

<section>
  <div class="step" style="left:69px"><div class="step-num">01</div><p>If you are going to use a passage of Lorem Ipsum, you need to be sure there isnt anything embarrassing hidden in the middle of text. All the Lorem Ipsum generators on the Internet tend to repeat.</p></div>
  <div class="step" style="left:315px"><div class="step-num">02</div><p>If you are going to use a passage of Lorem Ipsum, you need to be sure there isnt anything embarrassing hidden in the middle of text. All the Lorem Ipsum generators on the Internet tend to repeat.</p></div>
  <div class="step" style="left:558px"><div class="step-num">03</div><p>If you are going to use a passage of Lorem Ipsum, you need to be sure there isnt anything embarrassing hidden in the middle of text. All the Lorem Ipsum generators on the Internet tend to repeat.</p></div>
</section>

<section class="agents-band">
  <h2 class="section-title" style="left:81px;top:18px">Best Agents</h2>
  <div class="title-rule"></div>
  <div class="agent" style="left:83px">
    <div class="agent-photo" role="img" aria-label="Portrait of agent Theo Brandel" style="background:linear-gradient(#9aa0a6,#c9d3e0)"></div>
    <div class="agent-name">Theo Brandel</div><div class="agent-sub">Duis nisl massa, mol</div>
    <div class="stars">★★★★★</div>
  </div>
  <div class="agent" style="left:228px">
    <div class="agent-photo" role="img" aria-label="Portrait of agent Mira Oskett" style="background:linear-gradient(#f2f2f2,#2b2b2b)"></div>
    <div class="agent-name">Mira Oskett</div><div class="agent-sub">Duis accumsan erat n</div>
    <div class="stars">★★★<span class="off">★★</span></div>
  </div>
  <div class="agent" style="left:373px">
    <div class="agent-photo" role="img" aria-label="Portrait of agent Ines Varrow at a laptop" style="background:linear-gradient(135deg,#3a3a3a,#d9cfc3)"></div>
    <div class="agent-name">Ines Varrow</div><div class="agent-sub">Duis varius, arcu at</div>
    <div class="stars">★★★<span class="off">★★</span></div>
  </div>

  <h2 class="section-title" style="left:546px;top:18px">Reviews</h2>
  <div class="review" style="top:63px"><h3>Sed ultricies</h3><p>Sed ultricies justo quis viverra lacinia. Nunc vitae mattis turpis. Pellentesque quis sceleris-que sapien.</p></div>
  <div class="review" style="top:127px"><h3>Sed ultricies</h3><p>Sed ultricies justo quis viverra lacinia. Nunc vitae mattis turpis. Pellentesque quis sceleris-que sapien.</p></div>
  <div class="review" style="top:192px"><h3>Sed ultricies</h3><p>Sed ultricies justo quis viverra lacinia. Nunc vitae mattis turpis. Pellentesque quis sceleris-que sapien.</p></div>
</section>

<footer class="site-footer">
  <h4 class="f-head" style="left:82px">Information</h4>
  <ul class="f-links" style="left:82px"><li>About company</li><li>Our team</li><li>Registration</li><li>Payment Option</li><li>Infomation</li><li>FAQ</li></ul>
  <h4 class="f-head" style="left:173px">Useful Links</h4>
  <ul class="f-links" style="left:172px"><li>Homepage</li><li>404 page</li><li>Grid system</li><li>Our agents</li><li>Typography</li><li>Sitemap</li></ul>
  <h4 class="f-head" style="left:246px">Contacts</h4>
  <div class="f-phone">800 512 40 76</div>
  <div class="f-mail">info@zenvok.example</div>
  <div class="f-place">
    <svg width="7" height="10" viewBox="0 0 7 10" aria-hidden="true"><path d="M3.5 0a3.5 3.5 0 0 0-3.5 3.5C0 6 3.5 10 3.5 10S7 6 7 3.5A3.5 3.5 0 0 0 3.5 0z" fill="#999"/><circle cx="3.5" cy="3.5" r="1.3" fill="#232323"/></svg>
    <div><strong>Netherlands</strong><small>Lindengracht 14, Amsterdam 3/2</small></div>
  </div>
  <div class="f-social" aria-label="Social links">
    <span style="background:#2aa9e0"></span><span style="background:#3b5a9a"></span><span style="background:#d8432e"></span><span style="background:#d21f1f"></span><span style="background:#8a7d6f"></span>
  </div>
  <p class="f-note">All the Lorem Ipsum generators on the Internet tend to repeat predefined chunks as necessary, making this the first true generator on the Internet. It uses a dictionary of over 200 Latin words, combined with a handful of model sentence structures.</p>

  <span class="f-label" style="left:464px;top:27px">Your name:</span>
  <span class="f-label" style="left:598px;top:27px">E-mail:</span>
  <div class="f-input" style="left:464px;top:39px;width:123px;height:28px"></div>
  <div class="f-input" style="left:598px;top:39px;width:123px;height:28px"></div>
  <span class="f-label" style="left:464px;top:90px">Message:</span>
  <div class="f-input" style="left:464px;top:102px;width:259px;height:61px"></div>
  <div class="btn-send">SEND MESSAGE ›</div>
</footer>

<div class="copyright">© Copyright 2014 Zenvok · All Rights Reserved. Developed</div>

</body>
</html>
```